New website for our Escape Room

We are wanting to create a new website for our website. We have 2 different locations that guests will choose their location on the home page. Then we have 5 different escape room experiences. We like clean and fresh but fun. Our logo is black white and red. We like a modern feel that is simple to navigate. I love movement on the page. You can see our current site at quillhornpuzzles.com
We like fresh and modern. It needs to include much of the same information as out current site but we won't like the look of our site.

Target Market(s)

amusement, escape rooms.

Industry/Entity Type

escape room

Number of Pages Required

4 page

Requirements
Must have
• info on all 4 escape rooms, option to choose between Cedar Hollow and Ashford locations.

```html
<!DOCTYPE html>
<html lang="en">
<head>
<meta charset="utf-8">
<title>Quillhorn Escape Game</title>
<link rel="stylesheet" href="https://fonts.googleapis.com/css2?family=Anton&family=Oswald:wght@400;500;600;700&family=Poppins:wght@400;500;600&display=swap">
<style>
:root{
  --red:#e3131c;
  --red-deep:#8a0a10;
  --black:#0b0b0b;
  --dark:#171717;
  --panel:#222;
  --white:#ffffff;
  --mist:#eceded;
  --grey:#9a9a9a;
  --text-dark:#1a1a1a;
}
*{margin:0;padding:0;box-sizing:border-box}
html,body{width:1200px;height:4240px;overflow:hidden}
body{background:var(--black);font-family:"Poppins",sans-serif;color:var(--white);position:relative}
section,header,footer{position:absolute;left:0;width:1200px;overflow:hidden}
.display{font-family:"Anton",sans-serif;letter-spacing:3px;text-transform:uppercase;font-weight:400}
.kicker{font-family:"Oswald",sans-serif;color:var(--red);font-size:15px;letter-spacing:4px;text-transform:uppercase;font-weight:600}
.lede{font-size:14px;line-height:1.6}
.btn{display:inline-block;background:var(--red);color:var(--white);font-family:"Oswald",sans-serif;font-size:13px;letter-spacing:1px;text-transform:uppercase;padding:12px 26px;font-weight:600;white-space:nowrap}
.center{text-align:center}
.wordmark{font-family:"Anton",sans-serif;font-size:40px;letter-spacing:2px;color:var(--white);display:flex;align-items:center;gap:10px}
.wordmark .mark{width:14px;height:14px;background:var(--red)}

/* header + hero */
.hero{top:0;height:640px;background:linear-gradient(90deg,#0a0a0a 0%,#121212 45%,#1a0606 100%)}
.hero-art{position:absolute;right:0;top:0;width:620px;height:620px;background:radial-gradient(circle at 78% 22%,#e33a3a 0,#a1141a 14%,#3a0a0c 40%,#121212 75%)}
.site-header{top:0;height:110px;z-index:2;display:flex;align-items:center;padding:0 100px 0 190px}
.site-header .wordmark{margin-right:60px}
.nav{display:flex;gap:26px;font-family:"Oswald",sans-serif;font-size:15px;text-transform:uppercase;letter-spacing:1px}
.nav .active{color:var(--red)}
.site-header .btn{margin-left:auto}
.hero-copy{position:absolute;left:190px;top:270px;width:480px}
.hero-copy .kicker{color:var(--white);background:var(--red);padding:3px 10px;display:inline-block;font-size:14px}
.hero-copy h1{font-size:64px;margin:10px 0 14px;letter-spacing:6px}
.hero-copy .lede{color:#d8d8d8;margin-bottom:28px}

/* about */
.about{top:640px;height:520px;background:linear-gradient(180deg,#121212,#0b0b0b)}
.about-frame{position:absolute;left:190px;top:40px;width:400px;height:400px}
.about-photo{position:absolute;left:40px;top:30px;width:320px;height:340px;background:radial-gradient(circle at 55% 45%,#c9c9c9 0,#6f6f6f 35%,#1b1b1b 80%)}
.about-copy{position:absolute;left:640px;top:120px;width:420px;z-index:1}
.about-copy h2{font-size:44px}
.about-copy .kicker{margin:6px 0 14px}
.about-copy .lede{color:#cfcfcf;margin-bottom:26px;font-size:13px}
.ghost-word{position:absolute;right:-20px;bottom:-30px;font-family:"Anton",sans-serif;font-size:150px;color:rgba(255,255,255,.04);letter-spacing:4px}

/* locations */
.locations{top:1160px;height:560px;background:var(--white);color:var(--text-dark)}
.map-bg{position:absolute;left:200px;top:40px;width:800px;height:320px;background:radial-gradient(ellipse at center,#e6e6e6 0,#f7f7f7 60%,#fff 100%)}
.section-head{position:relative;padding-top:60px}
.section-head h2{font-size:42px;margin:4px 0 10px}
.section-head .lede{width:520px;margin:0 auto;font-size:13px;color:#555}
.loc-cards{position:absolute;top:220px;left:0;width:1200px;display:flex;justify-content:center;gap:40px}
.loc-card{width:350px;height:220px;transform:skewX(-8deg);border:3px solid var(--red);background:var(--white);box-shadow:0 10px 30px rgba(227,19,28,.25);overflow:hidden}
.loc-card .top{height:145px;background:linear-gradient(135deg,#d9d9d9,#f4f4f4 50%,#cfcfcf);display:flex;flex-direction:column;align-items:center;justify-content:center;transform:skewX(8deg)}
.loc-card .name{font-family:"Anton",sans-serif;font-size:40px;color:var(--text-dark);letter-spacing:2px}
.loc-card .sub{font-family:"Oswald",sans-serif;font-size:12px;letter-spacing:5px;color:var(--text-dark)}
.loc-card .city{font-family:"Oswald",sans-serif;font-size:11px;letter-spacing:2px;color:var(--text-dark);margin-top:2px}
.loc-card .bottom{transform:skewX(8deg);text-align:center;font-size:12px;font-weight:600;padding:16px 40px 0}
.locations .btn{position:absolute;left:540px;top:492px}

/* rooms */
.rooms{top:1720px;height:680px;background:linear-gradient(180deg,#0d0d0d 0%,#1a0708 60%,#0d0d0d 100%)}
.rooms .section-head .lede{color:#bbb}
.room-strip{position:absolute;top:240px;left:50px;width:1100px;display:flex;gap:8px}
.room{flex:1;transform:skewX(-14deg)}
.room .label{font-family:"Anton",sans-serif;font-size:20px;color:rgba(255,255,255,.75);text-align:center;letter-spacing:1px;padding:6px 0;background:#2a2a2a;white-space:nowrap;text-transform:uppercase}
.room .tile{height:230px;margin:8px 0;background:linear-gradient(160deg,#c4161d,#6d080c)}
.room .tile.light{background:linear-gradient(160deg,#f0f0f0,#b8b8b8)}
.room .tile span{display:block;width:100%;height:100%}
.room .label.red{background:var(--red);color:var(--white)}
.rooms .btn{position:absolute;left:540px;top:610px}

/* benefits */
.benefits{top:2400px;height:820px;background:linear-gradient(180deg,#f4f4f4 0%,#dcdcdc 70%,#c8c8c8 100%);color:var(--text-dark)}
.grave-bg{position:absolute;left:0;bottom:0;width:1200px;height:420px;background:linear-gradient(180deg,rgba(200,200,200,0),rgba(120,120,120,.35))}
.benefit{position:absolute;width:400px;height:160px;display:flex;align-items:center}
.benefit .badge{width:170px;height:170px;border-radius:50%;background:#1d1d1d;border:6px solid var(--white);position:relative;z-index:2;display:flex;align-items:center;justify-content:center;flex-shrink:0}
.benefit .badge svg{width:66px;height:66px;margin-top:-20px}
.benefit .badge em{position:absolute;bottom:22px;font-style:normal;font-family:"Oswald",sans-serif;font-size:11px;color:var(--text-dark);background:var(--white);padding:2px 12px;text-transform:uppercase}
.benefit .panel{margin-left:-60px;height:130px;flex:1;background:linear-gradient(135deg,var(--red),var(--red-deep));display:flex;align-items:center;justify-content:center;padding-left:60px;text-align:center}
.benefit h3{font-family:"Anton",sans-serif;font-size:22px;color:var(--white);letter-spacing:1px;line-height:1.15;text-transform:uppercase}

/* upgrade */
.upgrade{top:3220px;height:320px;background:linear-gradient(90deg,#141414,#1f1f1f 50%,#141414)}
.upgrade h2{position:absolute;left:190px;top:110px;font-size:40px}
.upgrade .lede{position:absolute;left:190px;top:170px;width:520px;color:#cfcfcf;font-size:13px}
.upgrade .btn{position:absolute;left:860px;top:140px}

/* audiences */
.audiences{top:3540px;height:370px;background:linear-gradient(180deg,#f5f5f5,#e3e3e3);color:var(--text-dark)}
.audiences h2{position:absolute;width:100%;top:60px;text-align:center;font-size:38px}
.aud-row{position:absolute;top:150px;left:0;width:1200px;display:flex;justify-content:center;gap:50px}
.aud{width:210px;text-align:center}
.aud svg{width:110px;height:110px}
.aud p{font-family:"Anton",sans-serif;font-size:21px;letter-spacing:1px;text-transform:uppercase;margin-top:10px;white-space:nowrap}

/* footer */
.site-footer{top:3910px;height:330px;background:#0c0c0c}
.foot-cols{position:absolute;top:60px;left:190px;display:flex;gap:70px}
.foot-col h4{font-family:"Anton",sans-serif;font-size:22px;letter-spacing:2px;text-transform:uppercase;border-bottom:3px solid var(--red);display:inline-block;margin-bottom:14px}
.foot-col ul{list-style:none;font-size:13px;line-height:1.9;color:#cfcfcf}
.contact-line{display:flex;align-items:center;gap:10px;font-size:13px;color:#cfcfcf;margin-top:16px;white-space:nowrap}
.contact-line svg{width:16px;height:16px}
.newsletter{display:flex;width:250px;margin-top:4px}
.newsletter span{flex:1;background:#1e1e1e;height:40px;font-size:12px;color:#888;padding:11px 12px}
.newsletter b{width:44px;height:40px;background:var(--red);display:flex;align-items:center;justify-content:center}
.socials{display:flex;gap:18px;margin-top:24px}
.socials i{width:14px;height:14px;border-radius:50%;background:#cfcfcf;display:block}
.foot-bar{position:absolute;bottom:0;left:0;width:1200px;height:60px;border-top:1px solid #262626;display:flex;align-items:center;justify-content:space-between;padding:0 190px;font-size:12px;color:#aaa}
</style>
</head>
<body>

<section class="hero">
  <div class="hero-art" role="img" aria-label="Haunted mansion silhouetted against a large red moon"></div>
  <div class="hero-copy">
    <span class="kicker">Escape rooms for every party</span>
    <h1 class="display">You cant hide</h1>
    <p class="lede">Lorem ipsum dolor sit amet, consectetur adipiscing elit, sed do eiusmod tempor incididunt ut labore et dolore magna aliqua.</p>
    <span class="btn">Find your location</span>
  </div>
</section>

<header class="site-header">
  <div class="wordmark"><span class="mark"></span>QUILLHORN</div>
  <nav class="nav"><span class="active">Home</span><span>About us</span><span>Escape rooms</span><span>FAQ</span><span>Gallery</span><span>Gift cards</span></nav>
  <span class="btn">Contact us</span>
</header>

<section class="about">
  <div class="about-frame">
    <svg width="400" height="400" viewBox="0 0 400 400"><polygon points="10,20 390,0 380,400 0,380" fill="none" stroke="#e3131c" stroke-width="14"/><polygon points="0,0 60,0 0,60" fill="#e3131c"/></svg>
    <div class="about-photo" role="img" aria-label="Dim black and white photo of a figure pressing a hand against glass"></div>
  </div>
  <div class="about-copy">
    <h2 class="display">About us</h2>
    <p class="kicker">Quillhorn Escape Game</p>
    <p class="lede">Quillhorn Escape Game is the heart-pounding, brain-twisting, time-bending room experience that will require everyone in your group's collective intellect, ingenuity, and problem-solving skills to escape.</p>
    <span class="btn">Learn more</span>
  </div>
  <div class="ghost-word">QUILLHORN</div>
</section>

<section class="locations">
  <div class="map-bg" role="img" aria-label="Faint world map backdrop"></div>
  <div class="section-head center">
    <p class="kicker">Quillhorn locations</p>
    <h2 class="display">Find the right location for you</h2>
    <p class="lede">Lorem ipsum dolor sit amet, consectetur adipiscing elit, sed do eiusmod tempor incididunt ut labore et dolore magna aliqua.</p>
  </div>
  <div class="loc-cards">
    <div class="loc-card">
      <div class="top"><span class="name">QUILLHORN</span><span class="sub">ESCAPE GAME</span><span class="city">— ASHFORD —</span></div>
      <p class="bottom">Wheelchair Accessible Rooms at Ashford Ward Nine</p>
    </div>
    <div class="loc-card">
      <div class="top"><span class="name">QUILLHORN</span><span class="sub">ESCAPE GAME</span><span class="city">— CEDAR HOLLOW —</span></div>
      <p class="bottom">Wheelchair Accessible Rooms at Cedar Hollow Snared, Hollow Lodge, Ward Nine</p>
    </div>
  </div>
  <span class="btn">Book now</span>
</section>

<section class="rooms">
  <div class="section-head center">
    <p class="kicker">Rooms locations</p>
    <h2 class="display">Find the right room for you</h2>
    <p class="lede">Lorem ipsum dolor sit amet, consectetur adipiscing elit, sed do eiusmod tempor incididunt ut labore et dolore magna aliqua.</p>
  </div>
  <div class="room-strip">
    <div class="room"><div class="label">Hollow lodge</div><div class="tile"><span role="img" aria-label="Hollow Lodge room artwork"></span></div><div class="label">Hollow lodge</div></div>
    <div class="room"><div class="label">Last signal</div><div class="tile"><span role="img" aria-label="Last Signal room artwork"></span></div><div class="label">Last signal</div></div>
    <div class="room"><div class="label">Iron keep</div><div class="tile light"><span role="img" aria-label="Iron Keep room artwork"></span></div><div class="label red">Iron keep</div></div>
    <div class="room"><div class="label">Snared</div><div class="tile"><span role="img" aria-label="Snared room artwork"></span></div><div class="label">Snared</div></div>
    <div class="room"><div class="label">Ward nine</div><div class="tile"><span role="img" aria-label="Ward Nine room artwork"></span></div><div class="label">Ward nine</div></div>
  </div>
  <span class="btn">Book now</span>
</section>

<section class="benefits">
  <div class="grave-bg" role="img" aria-label="Misty graveyard with tombstones"></div>
  <div class="section-head center">
    <p class="kicker">Benefits of escape rooms</p>
    <h2 class="display">Discover the benefits of escape rooms!</h2>
    <p class="lede">Escape rooms are fun team exercises that give you a sense of accomplishment.</p>
  </div>
  <div class="benefit" style="left:180px;top:230px">
    <div class="badge"><svg viewBox="0 0 60 60"><circle cx="20" cy="22" r="9" fill="#e3131c"/><circle cx="40" cy="22" r="9" fill="#e3131c"/><rect x="8" y="34" width="44" height="16" rx="8" fill="#e3131c"/></svg><em>Improve</em></div>
    <div class="panel"><h3>Communication<br>&amp; social skill</h3></div>
  </div>
  <div class="benefit" style="left:620px;top:230px">
    <div class="badge"><svg viewBox="0 0 60 60"><circle cx="30" cy="30" r="18" fill="none" stroke="#e3131c" stroke-width="8"/><circle cx="30" cy="30" r="6" fill="#e3131c"/></svg><em>Challenge</em></div>
    <div class="panel"><h3>Creative thinking<br>&amp; problem-solving<br>skills</h3></div>
  </div>
  <div class="benefit" style="left:180px;top:430px">
    <div class="badge"><svg viewBox="0 0 60 60"><ellipse cx="30" cy="30" rx="22" ry="18" fill="#e3131c"/><line x1="30" y1="12" x2="30" y2="48" stroke="#1d1d1d" stroke-width="3"/></svg><em>Enhance</em></div>
    <div class="panel"><h3>Build your<br>memory</h3></div>
  </div>
  <div class="benefit" style="left:620px;top:430px">
    <div class="badge"><svg viewBox="0 0 60 60"><circle cx="30" cy="30" r="22" fill="#e3131c"/><circle cx="22" cy="25" r="3" fill="#1d1d1d"/><circle cx="38" cy="25" r="3" fill="#1d1d1d"/><path d="M20 36 Q30 46 40 36" fill="none" stroke="#1d1d1d" stroke-width="3"/></svg><em>Improve</em></div>
    <div class="panel"><h3>Your mood</h3></div>
  </div>
  <div class="benefit" style="left:400px;top:630px">
    <div class="badge"><svg viewBox="0 0 60 60"><circle cx="26" cy="26" r="14" fill="none" stroke="#e3131c" stroke-width="6"/><line x1="36" y1="36" x2="50" y2="50" stroke="#e3131c" stroke-width="7"/></svg><em>Increase</em></div>
    <div class="panel"><h3>Attention to<br>detail</h3></div>
  </div>
</section>

<section class="upgrade" role="region" aria-label="Private experience">
  <h2 class="display">Upgrade to a private experience</h2>
  <p class="lede">Multiple parties can book the same room. If you would like to book a private experience, please contact us by phone.</p>
  <span class="btn">Upgrade now</span>
</section>

<section class="audiences">
  <h2 class="display">Quillhorn who</h2>
  <div class="aud-row">
    <div class="aud"><svg viewBox="0 0 110 110"><polygon points="55,4 101,30 101,80 55,106 9,80 9,30" fill="#fff" stroke="#e3131c" stroke-width="6"/><circle cx="42" cy="50" r="9" fill="#e3131c"/><circle cx="68" cy="50" r="9" fill="#e3131c"/><rect x="30" y="64" width="50" height="14" rx="7" fill="#e3131c"/></svg><p>Team building</p></div>
    <div class="aud"><svg viewBox="0 0 110 110"><polygon points="55,4 101,30 101,80 55,106 9,80 9,30" fill="#fff" stroke="#e3131c" stroke-width="6"/><rect x="28" y="44" width="54" height="26" rx="13" fill="#e3131c"/><rect x="38" y="54" width="12" height="4" fill="#fff"/><rect x="42" y="50" width="4" height="12" fill="#fff"/><circle cx="68" cy="56" r="3" fill="#fff"/></svg><p>Gamers</p></div>
    <div class="aud"><svg viewBox="0 0 110 110"><polygon points="55,4 101,30 101,80 55,106 9,80 9,30" fill="#fff" stroke="#e3131c" stroke-width="6"/><circle cx="40" cy="42" r="7" fill="#e3131c"/><circle cx="70" cy="42" r="7" fill="#e3131c"/><circle cx="55" cy="52" r="6" fill="#e3131c"/><rect x="32" y="54" width="16" height="24" fill="#e3131c"/><rect x="62" y="54" width="16" height="24" fill="#e3131c"/><rect x="49" y="62" width="12" height="16" fill="#e3131c"/></svg><p>Friends &amp; family</p></div>
    <div class="aud"><svg viewBox="0 0 110 110"><polygon points="55,4 101,30 101,80 55,106 9,80 9,30" fill="#fff" stroke="#e3131c" stroke-width="6"/><path d="M55 28 C42 28 36 38 36 46 C36 60 55 80 55 80 C55 80 74 60 74 46 C74 38 68 28 55 28Z" fill="#e3131c"/><circle cx="55" cy="46" r="7" fill="#fff"/></svg><p>Tourists &amp; visitors</p></div>
  </div>
</section>

<footer class="site-footer">
  <div class="foot-cols">
    <div class="foot-col" style="width:210px">
      <div class="wordmark"><span class="mark"></span>QUILLHORN</div>
      <div class="contact-line" style="margin-top:26px"><svg viewBox="0 0 16 16"><path d="M3 1 L6 1 L7 5 L5 6 C6 8 8 10 10 11 L11 9 L15 10 L15 13 C15 14 14 15 13 15 C6 15 1 10 1 3 C1 2 2 1 3 1Z" fill="#e3131c"/></svg>012-345-6789</div>
      <div class="contact-line"><svg viewBox="0 0 16 16"><rect x="1" y="3" width="14" height="10" fill="#e3131c"/><path d="M1 3 L8 9 L15 3" fill="none" stroke="#0c0c0c" stroke-width="1.5"/></svg>info@quillhornpuzzles.com</div>
    </div>
    <div class="foot-col" style="width:120px"><h4>Quick links</h4><ul><li>Home</li><li>FAQs</li><li>Blog</li><li>Gift cards</li></ul></div>
    <div class="foot-col" style="width:120px"><h4>Company</h4><ul><li>About us</li><li>Contact</li></ul></div>
    <div class="foot-col"><h4>Our newsletter</h4>
      <div class="newsletter"><span>Email address</span><b><svg width="16" height="16" viewBox="0 0 16 16"><path d="M1 8 L15 2 L11 15 L8 9 Z" fill="#fff"/></svg></b></div>
      <div class="socials"><i></i><i></i><i></i></div>
    </div>
  </div>
  <div class="foot-bar"><span>© 2022 QUILLHORN ESCAPE. All Rights Reserved.</span><span>Terms &amp; Conditions | Privacy Policy</span></div>
</footer>

</body>
</html>
```